Dental practice logo either "Molarbrook by Craft" or "Dental Lumora Clinic"

Dental practice with either of the logos mentioned above as we haven't decided on the name depends on which one looks better. Our motto of the practice is to create beautiful smiles and perform general dentistry.
Dr Oswin Halvereth
47 Tallowmere Road
Deeragun
Queensland 4814 and also the contact number, email address and website.
On the backside of the card it should be about the next appointment and also mention on the bottom" If unable to keep an appointment kindly give 24 hours notice otherwise a fee will be charged for the time reserved.
Reason: As it may take longer to design
We want the business card only on the dental practice named Dental Lumora Clinic and with a caption underneath the practice name as "Townsville's home of dentistry"
Target Market(s)
dental patients and general population who want beautiful smile
Industry/Entity Type
Dental
Look and feel

```html
<!DOCTYPE html>
<html lang="en">
<head>
<meta charset="UTF-8">
<title>Dental Lumora Clinic – Business Card</title>
<link href="https://fonts.googleapis.com/css2?family=Open+Sans:wght@400;600;700&display=swap" rel="stylesheet">
<style>
  :root {
    --orange: #f27a24;
    --orange-deep: #ea6a1c;
    --green: #7dc242;
    --white: #ffffff;
    --ink: #2e2e2e;
    --backdrop: #e8e6e3;
  }
  * { box-sizing: border-box; margin: 0; padding: 0; }
  html, body {
    width: 1200px; height: 872px; overflow: hidden;
    background: var(--backdrop);
    font-family: "Open Sans", Arial, sans-serif;
  }
  .sheet {
    position: relative; width: 1200px; height: 872px;
    display: flex; align-items: center; justify-content: center; gap: 60px;
  }
  .card {
    position: relative; width: 520px; height: 298px;
    background: var(--white); overflow: hidden;
    box-shadow: 0 6px 18px rgba(0,0,0,.18);
    display: flex; flex-direction: column;
  }
  .brand {
    display: flex; align-items: center; gap: 8px;
    font-size: 15px; font-weight: 600; letter-spacing: .5px; text-transform: uppercase;
  }
  .brand-dot { width: 14px; height: 14px; border-radius: 50%; border: 2px solid currentColor; flex: none; }

  /* back: appointment card */
  .appointment .band {
    height: 140px; background: var(--orange);
    border-bottom: 7px solid var(--green);
    padding: 20px 28px; color: var(--white);
    display: flex; flex-direction: column; justify-content: space-between;
  }
  .appointment .doctor { font-size: 28px; font-weight: 700; text-align: right; }
  .appointment .slots { flex: 1; padding: 18px 28px 0; }
  .slot { display: flex; align-items: flex-end; gap: 16px; margin-bottom: 14px; }
  .slot-label { width: 46px; font-size: 13px; font-weight: 600; color: var(--ink); }
  .slot-line {
    flex: 1; height: 14px;
    background: linear-gradient(90deg, #b9b9b9, #e6e6e6 85%, transparent);
  }
  .notice {
    padding: 0 28px 12px; font-size: 8.5px;
    color: var(--orange-deep); text-align: center;
  }

  /* front: contact card */
  .contact .head {
    height: 118px; padding: 20px 28px;
    display: flex; flex-direction: column; justify-content: space-between;
  }
  .contact .brand { color: var(--orange); }
  .contact .doctor { font-size: 28px; font-weight: 700; color: var(--ink); text-align: right; }
  .contact .band {
    flex: 1; list-style: none; background: var(--orange); border-top: 7px solid var(--green);
    padding: 20px 28px; color: var(--white);
    display: flex; flex-direction: column; justify-content: center; gap: 9px;
  }
  .detail { display: flex; align-items: center; gap: 12px; font-size: 14px; white-space: nowrap; }
  .detail svg { width: 22px; height: 22px; flex: none; }
</style>
</head>
<body>
<main class="sheet">

  <section class="card appointment">
    <header class="band">
      <div class="brand"><span class="brand-dot"></span>Dental Lumora Clinic</div>
      <h1 class="doctor">Dr. Oswin Halvereth</h1>
    </header>
    <div class="slots">
      <div class="slot"><span class="slot-label">Day</span><span class="slot-line"></span></div>
      <div class="slot"><span class="slot-label">Date</span><span class="slot-line"></span></div>
      <div class="slot"><span class="slot-label">Time</span><span class="slot-line"></span></div>
    </div>
    <p class="notice">If unable to keep an appointment kindly give 24 hours notice otherwise a fee will be charged for the time reserved.</p>
  </section>

  <section class="card contact">
    <header class="head">
      <div class="brand"><span class="brand-dot"></span>Dental Lumora Clinic</div>
      <h1 class="doctor">Dr. Oswin Halvereth</h1>
    </header>
    <ul class="band">
      <li class="detail">
        <svg viewBox="0 0 22 22"><circle cx="11" cy="11" r="11" fill="#fff"/><path d="M11 5a4 4 0 0 0-4 4c0 3 4 8 4 8s4-5 4-8a4 4 0 0 0-4-4zm0 5.5a1.5 1.5 0 1 1 0-3 1.5 1.5 0 0 1 0 3z" fill="#f27a24"/></svg>
        47 Tallowmere Road, Harrowdene, Northvale 4907
      </li>
      <li class="detail">
        <svg viewBox="0 0 22 22"><circle cx="11" cy="11" r="11" fill="#fff"/><path d="M8 5.5l2 3-1.3 1.2c.7 1.5 1.9 2.7 3.4 3.4L13.4 12l3 2-.8 2c-4.6.2-9-4.2-8.8-8.8z" fill="#f27a24"/></svg>
        xxxx xxx x xxx
      </li>
      <li class="detail">
        <svg viewBox="0 0 22 22"><circle cx="11" cy="11" r="11" fill="#fff"/><rect x="5.5" y="7" width="11" height="8" fill="#f27a24"/><path d="M5.5 7l5.5 4.5L16.5 7" stroke="#fff" stroke-width="1.2" fill="none"/></svg>
        hello@lumoraclinic.com
      </li>
      <li class="detail">
        <svg viewBox="0 0 22 22"><circle cx="11" cy="11" r="11" fill="#fff"/><g stroke="#f27a24" stroke-width="1.3" fill="none"><circle cx="11" cy="11" r="5.5"/><ellipse cx="11" cy="11" rx="2.4" ry="5.5"/><path d="M5.5 11h11"/></g></svg>
        www.lumoraclinic.com
      </li>
    </ul>
  </section>

</main>
</body>
</html>
```